Car Loan Landing Page Redesign

We are looking for a fresh, eye catching and professional redesign of our landing page as attached.
This current template doesn't stand out and doesn't highlight the main part of the page which is the application box.
Our corporate colors are pink #ee245f, black #000, #232323 and colors as in our website www.brindle.com.au
Brindle is Australia's leading car finance brokerage institution and this landing page is geared towards car finance.
We also believe the background banner needs some sort of creative approach.
We also feel that the form steps (once you click on start to compare) needs to be refreshed as well in terms of its form input fields design.
We like to have this whole page redesigned and freshen up so it gives an unique design experience to the users.
Feel free to use your imagination with some great eye catchy banner, and move the elements around as you need to.
Target Market(s)
Australians who are looking for car finance
Industry/Entity Type
Finance
Number of Pages Required
1 page
Font styles to use
Other font styles liked:
- Roboto
Look and feel
Each slider illustrates characteristics of the customer's brand and the style your logo design should communicate.

```html
<!DOCTYPE html>
<html lang="en">
<head>
<meta charset="utf-8">
<title>Brindle – Car Finance</title>
<link href="https://fonts.googleapis.com/css2?family=Roboto:wght@300;400;500;700;900&display=swap" rel="stylesheet">
<style>
:root{
  --pink:#ee245f;
  --black:#000;
  --ink:#232323;
  --text:#555;
  --muted:#8a8a8a;
  --line:#e4e4e4;
  --panel:#f4f4f4;
  --white:#fff;
  --footer:#1a1b24;
  --footer-text:#b9bac2;
}
*{box-sizing:border-box;margin:0;padding:0}
html,body{width:1200px;height:3175px;overflow:hidden}
body{font-family:'Roboto',Arial,sans-serif;color:var(--ink);background:var(--white);position:relative}
a{color:inherit;text-decoration:none}
.abs{position:absolute}

/* header */
.site-header{position:absolute;left:0;top:0;width:1200px;height:64px;background:var(--white)}
.brand{position:absolute;left:144px;top:8px;font-size:38px;font-weight:400;color:var(--ink);letter-spacing:-.5px;line-height:1}
.brand small{display:block;font-size:9px;letter-spacing:1px;margin-top:1px;color:var(--text)}
.header-phone{position:absolute;left:940px;top:17px;width:114px;height:30px;border:2px solid var(--pink);border-radius:15px;color:var(--pink);font-size:12px;display:flex;align-items:center;justify-content:center}

/* hero */
.hero{position:absolute;left:0;top:64px;width:1200px;height:576px;
  background:radial-gradient(ellipse 40% 55% at 50% 40%,#3b3f46 0%,#202329 45%,transparent 75%),
  linear-gradient(180deg,#8a7a55 0%,#4c4a3b 30%,#25282a 60%,#0e0f11 100%)}
.hero-title{position:absolute;left:0;top:356px;width:1200px;text-align:center;color:var(--white);font-weight:500;font-size:36px;line-height:42px}
.hero-title span{text-transform:uppercase}
.btn{display:flex;align-items:center;justify-content:center;gap:10px;border-radius:22px;font-size:13px;font-weight:700;letter-spacing:.8px;text-transform:uppercase}
.btn-outline{position:absolute;border:2px solid var(--pink);color:var(--pink)}
.btn-solid{position:absolute;background:var(--pink);color:var(--white)}
.btn-white{position:absolute;background:var(--white);color:var(--pink)}

/* savings card */
.savings-card{position:absolute;left:144px;top:603px;width:910px;height:614px;background:var(--white);box-shadow:0 12px 40px rgba(0,0,0,.12)}
.section-title{text-align:center;font-weight:900;font-size:27px;line-height:32px;text-transform:uppercase;color:var(--ink)}
.section-sub{text-align:center;font-size:14px;color:var(--muted);line-height:22px}
.step{position:absolute;width:300px;text-align:center}
.step-icon{width:76px;height:76px;margin:0 auto;border-radius:50%;display:flex;align-items:center;justify-content:center}
.step-icon.active{border:1px dashed var(--pink)}
.step h3{font-size:19px;font-weight:500;margin-top:20px;color:var(--ink)}
.step p{font-size:12px;color:var(--muted);line-height:21px;margin:14px auto 0;width:190px}
.read-more{display:inline-block;font-size:12px;color:var(--text);margin-top:12px}
.read-more::after{content:" →"}
.step-divider{position:absolute;top:160px;width:1px;height:150px;background:var(--line)}
.step-arrow{position:absolute;width:14px;height:14px;border-radius:50%;background:var(--white);border:1px solid var(--line);font-size:9px;display:flex;align-items:center;justify-content:center;color:var(--ink)}

/* borrow box */
.borrow-box{position:absolute;left:275px;top:1033px;width:650px;height:378px;background:var(--panel);border-radius:4px}
.amount{position:absolute;left:226px;top:131px;width:197px;height:36px;background:var(--white);border:1px solid var(--line);color:var(--pink);font-size:20px;font-weight:700;display:flex;align-items:center;justify-content:center}
.slider-track{position:absolute;left:42px;top:218px;width:565px;display:flex;gap:6px}
.slider-track i{flex:1;height:3px;background:#e2e2e2;border-radius:2px}
.slider-labels{position:absolute;left:30px;top:243px;width:590px;display:flex;justify-content:space-between;font-size:11px;color:var(--text)}

/* lenders */
.lenders{position:absolute;left:232px;top:1600px;width:736px;display:flex;align-items:center;justify-content:space-between}
.lender{font-size:21px;font-weight:700;color:var(--ink);display:flex;align-items:center;gap:6px}
.lender .dot{width:18px;height:18px;border-radius:50%;background:var(--ink)}
.lender .sq{width:10px;height:10px;background:var(--ink)}

/* features */
.features{position:absolute;left:0;top:1703px;width:1200px;height:519px;background:var(--panel)}
.feature{position:absolute;width:300px;text-align:center}
.feature-icon{height:46px;display:flex;align-items:center;justify-content:center}
.feature h4{font-size:13px;font-weight:700;text-transform:uppercase;margin-top:8px;letter-spacing:.3px}
.feature p{font-size:12px;color:var(--muted);line-height:20px;width:250px;margin:8px auto 0}
.feature .read-more{margin-top:14px}

/* how section */
.how-item{position:absolute;width:218px;font-size:12px;line-height:19px;color:var(--muted)}
.how-item.right{text-align:right}
.how-icon{position:absolute;width:44px;height:44px;border-radius:50%;display:flex;align-items:center;justify-content:center}
.how-icon.light{background:var(--white);box-shadow:0 2px 8px rgba(0,0,0,.12)}
.how-icon.dark{background:var(--ink)}
.how-line{position:absolute;height:0;border-top:1px dashed #c9c9c9}
.car-plan{position:absolute;left:504px;top:2387px;width:241px;height:370px;border-radius:90px 90px 30px 30px;background:linear-gradient(180deg,#f2f2f2,#d8d8d8 50%,#eeeeee)}

/* cta band */
.cta-band{position:absolute;left:0;top:2757px;width:1200px;height:89px;background:var(--pink)}
.cta-band p{position:absolute;left:144px;top:32px;color:var(--white);font-size:18px;font-weight:700}

/* footer */
.site-footer{position:absolute;left:0;top:2846px;width:1200px;height:329px;background:var(--footer);color:var(--footer-text)}
.footer-brand{position:absolute;left:144px;top:60px;font-size:38px;color:var(--white);line-height:1}
.footer-brand small{display:block;font-size:9px;letter-spacing:1px;color:var(--footer-text)}
.footer-about{position:absolute;left:144px;top:120px;width:270px;font-size:11px;line-height:18px}
.footer-col{position:absolute;top:60px}
.footer-col h5{color:var(--white);font-size:12px;font-weight:700;letter-spacing:.8px;margin-bottom:22px}
.footer-col li{list-style:none;font-size:11px;line-height:22px}
.contact li{display:flex;gap:10px;align-items:flex-start;margin-bottom:12px;line-height:18px}
.social{display:grid;grid-template-columns:110px 110px;row-gap:12px}
.social li{display:flex;align-items:center;gap:8px}
.social i{width:14px;height:14px;background:var(--footer-text);border-radius:2px}
.footer-rule{position:absolute;left:144px;top:248px;width:912px;height:1px;background:#3a3b46}
.legal{position:absolute;left:144px;top:267px;font-size:11px;line-height:18px}
.legal b{color:var(--pink);font-weight:400}
.badges{position:absolute;left:780px;top:260px;display:flex;gap:22px;align-items:center}
.badges span{display:block;background:#d9d9de}
</style>
</head>
<body>

<header class="site-header">
  <div class="brand">Brindle<small>finance + insurance</small></div>
  <a class="header-phone">+ 1300 555 218</a>
</header>

<section class="hero">
  <div class="abs" style="inset:0" role="img" aria-label="Dark sports car parked on a road with warm sunset trees behind"></div>
  <h1 class="hero-title"><span>Brindle has helped over</span><br>35,000 Australians with their finance!</h1>
  <a class="btn btn-outline" style="left:480px;top:461px;width:238px;height:40px">Start to compare
    <svg width="16" height="10" viewBox="0 0 16 10"><path d="M0 5h14M10 1l4 4-4 4" stroke="currentColor" stroke-width="1.6" fill="none"/></svg></a>
</section>

<section class="savings-card">
  <h2 class="section-title" style="position:absolute;left:0;top:32px;width:910px">How much can you save<br>on your car loan?</h2>
  <p class="section-sub" style="position:absolute;left:0;top:100px;width:910px">Comparing car loan lenders could save you thousands!</p>

  <div class="step" style="left:0;top:174px">
    <div class="step-icon"><svg width="40" height="44" viewBox="0 0 40 44"><rect x="5" y="3" width="28" height="38" rx="2" fill="none" stroke="#ee245f" stroke-width="2"/><path d="M11 13l3 3 5-6M11 23l3 3 5-6M11 33l3 3 5-6M23 14h6M23 24h6M23 34h6" stroke="#232323" stroke-width="2" fill="none"/></svg></div>
    <h3>Step 1</h3>
    <p>Tell us how much you need for your next car.</p>
    <a class="read-more">Read More</a>
  </div>
  <div class="step-divider" style="left:300px"></div>
  <div class="step-arrow" style="left:293px;top:258px">›</div>

  <div class="step" style="left:305px;top:174px">
    <div class="step-icon active"><svg width="34" height="34" viewBox="0 0 34 34"><path d="M6 28L28 6" stroke="#ee245f" stroke-width="2.5"/><circle cx="9" cy="9" r="4" fill="none" stroke="#ee245f" stroke-width="2.5"/><circle cx="25" cy="25" r="4" fill="none" stroke="#ee245f" stroke-width="2.5"/></svg></div>
    <h3>Step 2</h3>
    <p>We provide lightning quick quotes from our lenders</p>
    <a class="read-more">Read More</a>
  </div>
  <div class="step-divider" style="left:611px"></div>
  <div class="step-arrow" style="left:604px;top:258px">›</div>

  <div class="step" style="left:616px;top:174px">
    <div class="step-icon"><svg width="50" height="34" viewBox="0 0 50 34"><path d="M7 16l5-10h26l5 10v12H7z" fill="none" stroke="#ee245f" stroke-width="2.2"/><path d="M10 28v4h6v-4M34 28v4h6v-4M7 16h36" stroke="#ee245f" stroke-width="2.2" fill="none"/><circle cx="14" cy="22" r="2.5" fill="#232323"/><circle cx="36" cy="22" r="2.5" fill="#232323"/><path d="M20 22h10" stroke="#232323" stroke-width="2"/></svg></div>
    <h3>Step 3</h3>
    <p>Gain approval and drive away with a better deal!</p>
    <a class="read-more">Read More</a>
  </div>
</section>

<section class="borrow-box">
  <h2 class="section-title" style="position:absolute;left:0;top:52px;width:650px;font-size:26px;line-height:31px">How much do you like<br>to borrow ?</h2>
  <div class="amount">$5,000</div>
  <div class="slider-track"><i></i><i></i><i></i><i></i><i></i><i></i><i></i><i></i><i></i><i></i><i></i><i></i></div>
  <svg class="abs" style="left:37px;top:190px" width="22" height="30" viewBox="0 0 22 30"><path d="M11 29C4 19 1 15 1 10a10 10 0 0 1 20 0c0 5-3 9-10 19z" fill="#ee245f"/><circle cx="11" cy="10" r="4" fill="#fff"/></svg>
  <div class="slider-labels"><span>$5k</span><span>$15k</span><span>$24k</span><span>$34k</span><span>$43k</span><span>$53k</span><span>$60k</span><span>$72k</span><span>$82k</span><span>$91k</span><span>$101k</span><span>$110k</span><span>$120k</span></div>
  <a class="btn btn-solid" style="left:206px;top:283px;width:240px;height:38px">Start to compare
    <svg width="16" height="10" viewBox="0 0 16 10"><path d="M0 5h14M10 1l4 4-4 4" stroke="currentColor" stroke-width="1.6" fill="none"/></svg></a>
</section>

<h2 class="section-title abs" style="left:0;top:1462px;width:1200px;font-size:28px;line-height:31px">Compare multiple lenders &amp; save on<br>your finance. Get Brindle</h2>
<p class="section-sub abs" style="left:320px;top:1530px;width:560px">Comparing lenders can help you get great rates and save thousands! Compare Australia's top lenders with Brindle and save.</p>

<div class="lenders">
  <span class="lender">Tallwood</span>
  <span class="lender" style="background:var(--ink);color:#fff;padding:4px 10px">Kestrel</span>
  <span class="lender">Northbank</span>
  <span class="lender"><span class="dot"></span>Marlin</span>
  <span class="lender"><span class="sq"></span>ORBIS</span>
  <span class="lender">Coastline</span>
</div>

<section class="features">
  <div class="feature" style="left:127px;top:52px">
    <div class="feature-icon"><svg width="44" height="40" viewBox="0 0 44 40"><rect x="4" y="12" width="9" height="26" rx="3" fill="#232323"/><rect x="17.5" y="6" width="9" height="32" rx="3" fill="#ee245f"/><rect x="31" y="12" width="9" height="26" rx="3" fill="#232323"/></svg></div>
    <h4>Australia's top lenders</h4>
    <p>Accredited with the NFBA. Brindle deals with over 25 of Australia's top rated lenders all eager for your business.</p>
    <a class="read-more">Read More</a>
  </div>
  <div class="feature" style="left:449px;top:52px">
    <div class="feature-icon"><svg width="44" height="40" viewBox="0 0 44 40"><path d="M4 14l10-8 8 6 10-9 8 6" stroke="#ee245f" stroke-width="2" fill="none"/><rect x="6" y="22" width="5" height="16" fill="#232323"/><rect x="15" y="18" width="5" height="20" fill="#232323"/><rect x="24" y="20" width="5" height="18" fill="#232323"/><rect x="33" y="16" width="5" height="22" fill="#232323"/></svg></div>
    <h4>Compare &amp; save</h4>
    <p>Gain the Brindle advantage as our financial professionals scout the market for a car loan that will save you thousands.</p>
    <a class="read-more">Read More</a>
  </div>
  <div class="feature" style="left:760px;top:52px">
    <div class="feature-icon"><svg width="40" height="40" viewBox="0 0 40 40"><path d="M8 34L32 6" stroke="#232323" stroke-width="3"/><circle cx="10" cy="10" r="5" fill="none" stroke="#ee245f" stroke-width="3"/><circle cx="30" cy="30" r="5" fill="none" stroke="#ee245f" stroke-width="3"/></svg></div>
    <h4>Low interest rates</h4>
    <p>If you want lower interest rates, trust Brindle. We don't rest until we've found the lowest, most competitive rates for your loan.</p>
    <a class="read-more">Read More</a>
  </div>

  <div class="feature" style="left:127px;top:280px">
    <div class="feature-icon"><svg width="42" height="42" viewBox="0 0 42 42"><circle cx="21" cy="21" r="19" fill="#232323"/><path d="M21 9v13h9" stroke="#ee245f" stroke-width="3" fill="none"/></svg></div>
    <h4 style="text-transform:none">Quick Approvals</h4>
    <p>Need wheels fast? We can turn around approvals on the same day, approved customers! We make it easy.</p>
    <a class="read-more">Read More</a>
  </div>
  <div class="feature" style="left:449px;top:280px">
    <div class="feature-icon"><svg width="38" height="44" viewBox="0 0 38 44"><path d="M13 4h12l-4 8h-4z" fill="#232323"/><path d="M15 12h8c10 6 13 14 13 20 0 7-6 10-17 10S2 39 2 32c0-6 3-14 13-20z" fill="#232323"/><text x="19" y="34" text-anchor="middle" font-family="Roboto,sans-serif" font-size="14" font-weight="700" fill="#ee245f">$</text></svg></div>
    <h4>Bad credit OK</h4>
    <p>Do you have bad credit? Our financial professionals help people with bad credit get a second chance at car finance.</p>
    <a class="read-more">Read More</a>
  </div>
  <div class="feature" style="left:760px;top:280px">
    <div class="feature-icon"><svg width="42" height="42" viewBox="0 0 42 42"><circle cx="21" cy="21" r="19" fill="#232323"/><path d="M12 21l6 6 12-12" stroke="#ee245f" stroke-width="3.5" fill="none"/></svg></div>
    <h4>No obligation</h4>
    <p>Get a quote, look and see how much you can save with Brindle. There's no obligation to apply.</p>
    <a class="read-more">Read More</a>
  </div>
</section>

<h2 class="section-title abs" style="left:0;top:2284px;width:1200px;font-size:27px;line-height:31px">How Brindle will help you find a great<br>deal on your car finance</h2>

<div class="car-plan" role="img" aria-label="Top-down technical line drawing of a car showing its interior layout"></div>

<p class="how-item" style="left:144px;top:2398px">Understand your needs and requirements and find a tailored loan</p>
<div class="how-line" style="left:144px;top:2468px;width:242px"></div>
<div class="how-icon light" style="left:386px;top:2424px"><svg width="18" height="18" viewBox="0 0 18 18"><path d="M17 1L1 8l7 2 2 7z" fill="#232323"/></svg></div>

<p class="how-item" style="left:144px;top:2521px">Ascertain your borrowing power, your capacity for repayments so you</p>
<div class="how-line" style="left:144px;top:2593px;width:242px"></div>
<div class="how-icon light" style="left:386px;top:2549px"><svg width="16" height="22" viewBox="0 0 16 22"><path d="M8 21C3 14 1 11 1 8a7 7 0 0 1 14 0c0 3-2 6-7 13z" fill="#ee245f"/><circle cx="8" cy="8" r="3" fill="#fff"/></svg></div>

<p class="how-item" style="left:144px;top:2639px">Compare your car loan with 256 lenders and banks so you gain the best deal</p>
<div class="how-line" style="left:144px;top:2705px;width:242px"></div>
<div class="how-icon light" style="left:386px;top:2661px"><svg width="18" height="20" viewBox="0 0 18 20"><rect x="2" y="1" width="14" height="18" rx="1" fill="none" stroke="#232323" stroke-width="1.6"/><path d="M6 14l3-8 3 8M7 11h4" stroke="#232323" stroke-width="1.4" fill="none"/></svg></div>

<p class="how-item right" style="left:836px;top:2400px">Explain all fees, charges and obligations up front so you know exactly what</p>
<div class="how-line" style="left:812px;top:2470px;width:242px"></div>
<div class="how-icon light" style="left:767px;top:2426px"><svg width="22" height="16" viewBox="0 0 22 16"><path d="M3 7l3-5h10l3 5v6H3z" fill="#232323"/><circle cx="7" cy="10" r="1.5" fill="#fff"/><circle cx="15" cy="10" r="1.5" fill="#fff"/></svg></div>

<p class="how-item right" style="left:836px;top:2521px">Provide you with a dedicated personal consultant to manage your application</p>
<div class="how-line" style="left:812px;top:2589px;width:242px"></div>
<div class="how-icon light" style="left:767px;top:2545px"><svg width="22" height="22" viewBox="0 0 22 22"><circle cx="11" cy="11" r="9.5" fill="none" stroke="#232323" stroke-width="1.6"/><text x="11" y="16" text-anchor="middle" font-family="Roboto,sans-serif" font-size="13" font-weight="700" fill="#232323">$</text></svg></div>

<p class="how-item right" style="left:836px;top:2639px">Provide you with the highest level of customer service and support</p>
<div class="how-line" style="left:812px;top:2705px;width:242px"></div>
<div class="how-icon dark" style="left:767px;top:2661px"><svg width="20" height="16" viewBox="0 0 20 16"><path d="M2 8l5 5L18 2" stroke="#fff" stroke-width="3" fill="none"/></svg></div>

<section class="cta-band">
  <p>Compare Australia's top lenders with us today. Get Brindle!</p>
  <a class="btn btn-white" style="left:815px;top:24px;width:239px;height:42px">Start to compare
    <svg width="16" height="10" viewBox="0 0 16 10"><path d="M0 5h14M10 1l4 4-4 4" stroke="currentColor" stroke-width="1.6" fill="none"/></svg></a>
</section>

<footer class="site-footer">
  <div class="footer-brand">Brindle<small>finance + insurance</small></div>
  <p class="footer-about">Simple car finance for every driver, with friendly brokers who compare top lenders, explain each fee and find a loan that suits your budget and your next car.</p>

  <div class="footer-col" style="left:463px">
    <h5>QUICK LINKS</h5>
    <ul><li>Home</li><li>About Us</li><li>Services</li><li>Testimonials</li><li>Contact Us</li></ul>
  </div>

  <div class="footer-col" style="left:612px">
    <h5>CONTACT US</h5>
    <ul class="contact">
      <li><svg width="12" height="12" viewBox="0 0 12 12"><path d="M2 1h3l1 3-2 1a7 7 0 0 0 3 3l1-2 3 1v3c-6 0-9-3-9-9z" fill="#ee245f"/></svg>+ 1300 555 218</li>
      <li><svg width="12" height="14" viewBox="0 0 12 14"><path d="M6 13C2 8 1 6 1 5a5 5 0 0 1 10 0c0 1-1 3-5 8z" fill="#ee245f"/></svg>48 Harbour Row Geelong,<br>VIC 3220</li>
      <li><svg width="12" height="10" viewBox="0 0 12 10"><rect width="12" height="10" rx="1" fill="#ee245f"/><path d="M0 1l6 4 6-4" stroke="#1a1b24" fill="none"/></svg>info@brindle.com.au</li>
    </ul>
  </div>

  <div class="footer-col" style="left:844px">
    <h5>SOCIAL LINKS</h5>
    <ul class="social">
      <li><i></i>Friendlink</li><li><i></i>Circlenet</li>
      <li><i></i>Chirpline</li><li><i></i>Workweb</li>
      <li><i></i>Vidstream</li><li><i></i>Pinboard</li>
    </ul>
  </div>

  <div class="footer-rule"></div>
  <p class="legal"><b>© 2016 All rights reserved.</b> Quantum Brindle Pty Ltd · ABN: 98 765 432 109, Australian Credit Licence 523817<br>Free Phone: 1300 555 218</p>
  <div class="badges">
    <span style="width:28px;height:36px"></span>
    <span style="width:96px;height:22px;border-radius:11px"></span>
    <span style="width:58px;height:24px"></span>
  </div>
</footer>

</body>
</html>
```